Meridale Cleaning Services

In need of a business card design suited for a growing cleaning company.

We offer our cleaning and maintenance services to a wide range of clients including but not limited to the following: constuction industry, hospitality, commercial, industrial and domestic

I want the card to be very noticable, i would like people to say 'hey, great card!' when i hand them my card.double sided would be nice

we want our business to come across as exceedingly professional and innovative (different).

a contemporary design is what we have in mind
we want to present an image of a quality business with a high standard of excellence in consistent service.

i just really need a card that persuades top end quality,
our business is very certified and also strives towards environmentaly friendly alternatives
Updates

hey sorry, i have uploaded my company logo design and name
cheers.

hey guys i have added my company logo/name file on my brief page. many thanks

sorry guys a typo in the brief..
address is Tolley Rd. not Tolly Rd
thanks

Industry/Entity Type

Industrial

Requirements
Must have
• company name: meridale cleaning services
operations manager: Colm Varetti
Tel: (02)9373 6204
Fax: (02)8645 7712
Mob: 0438571490

address: 47 Tolly RD Pymble NSW 2073
Postal Adress: PO Box 5832 North Ryde NSW 2113
email: meridaleclean@wexanet.com.au
website: meridalecleaningservices.com.au

```html
<!DOCTYPE html>
<html lang="en">
<head>
<meta charset="utf-8">
<title>Meridale Cleaning Services – Business Card</title>
<link rel="stylesheet" href="https://fonts.googleapis.com/css2?family=Roboto+Condensed:wght@400;700&family=Open+Sans:wght@400;700&display=swap">
<style>
  :root {
    --canvas-bg: #e6eaee;
    --card-white: #f7f7f7;
    --stripe-dark: #2b2b2d;
    --brand-green: #3d9a1b;
    --brand-blue: #52c3f1;
    --logo-blue: #1f7fd6;
    --ink: #1b1b1b;
    --text-light: #ffffff;
    --text-muted: #a9a9a9;
    --label: #2a2a2a;
  }
  * { box-sizing: border-box; margin: 0; padding: 0; }
  html, body { width: 1200px; height: 900px; overflow: hidden; }
  body {
    background: var(--canvas-bg);
    font-family: "Roboto Condensed", "Arial Narrow", sans-serif;
    position: relative;
  }
  .side-label {
    position: absolute;
    font-family: "Open Sans", sans-serif;
    font-size: 30px;
    color: var(--label);
  }
  .side-label--front { left: 300px; top: 50px; }
  .side-label--back { left: 840px; top: 830px; }

  .card {
    position: absolute;
    width: 560px;
    height: 340px;
    border-radius: 16px;
    overflow: hidden;
    background: var(--card-white);
    box-shadow: 0 8px 22px rgba(0,0,0,0.22);
  }
  .card--front { left: 70px; top: 110px; }
  .card--back { left: 570px; top: 460px; }
  .card-shapes { position: absolute; inset: 0; }

  /* front */
  .brand {
    position: absolute;
    right: 26px;
    top: 22px;
    display: flex;
    align-items: center;
    gap: 10px;
  }
  .brand-dot {
    width: 34px; height: 34px; border-radius: 50%;
    background: var(--logo-blue);
  }
  .brand-name {
    font-weight: 700;
    font-size: 21px;
    color: var(--logo-blue);
    line-height: 1.05;
    width: 160px;
  }
  .contact-phones {
    position: absolute;
    left: 62px;
    top: 122px;
    color: var(--text-light);
    font-size: 14px;
    line-height: 1.25;
  }
  .person {
    position: absolute;
    left: 140px;
    top: 232px;
    transform: rotate(-30deg);
    transform-origin: left top;
    font-weight: 700;
    line-height: 1.1;
  }
  .person-name { font-size: 24px; color: var(--text-light); }
  .person-role { font-size: 18px; color: var(--ink); }
  .contact-address {
    position: absolute;
    left: 330px;
    top: 262px;
    font-size: 14px;
    line-height: 1.2;
    color: var(--ink);
  }

  /* back */
  .back-brand {
    position: absolute;
    left: 0; right: 0; top: 118px;
    display: flex;
    flex-direction: column;
    align-items: center;
    gap: 10px;
  }
  .back-brand .brand-dot { width: 54px; height: 54px; }
  .back-brand .brand-name { width: auto; font-size: 20px; }
  .website {
    position: absolute;
    left: 0; right: 0; top: 288px;
    text-align: center;
    color: var(--text-muted);
    font-size: 14px;
    letter-spacing: 0.3px;
  }
</style>
</head>
<body>
  <div class="side-label side-label--front">Front</div>

  <section class="card card--front">
    <svg class="card-shapes" width="560" height="340" viewBox="0 0 560 340" aria-hidden="true">
      <rect x="0" y="0" width="46" height="340" fill="var(--stripe-dark)"/>
      <polygon points="46,100 430,100 300,300 46,300" fill="var(--brand-green)"/>
      <polygon points="560,150 560,340 190,340" fill="var(--brand-blue)"/>
    </svg>

    <div class="brand">
      <span class="brand-dot"></span>
      <span class="brand-name">Meridale Cleaning Services</span>
    </div>

    <div class="contact-phones">
      <div>Tel: (02)9373 6204</div>
      <div>Fax: (02)8645 7712</div>
      <div>Mob: 0438571490</div>
    </div>

    <div class="person">
      <div class="person-name">Colm Varetti</div>
      <div class="person-role">(operations manager)</div>
    </div>

    <div class="contact-address">
      <div>47 Tolly RD Pymble NSW 2073</div>
      <div>PO Box 5832 North Ryde NSW 2113</div>
      <div>email: meridaleclean@wexanet.com.au</div>
    </div>
  </section>

  <section class="card card--back">
    <svg class="card-shapes" width="560" height="340" viewBox="0 0 560 340" aria-hidden="true">
      <rect x="0" y="0" width="560" height="78" fill="var(--stripe-dark)"/>
      <rect x="0" y="250" width="560" height="90" fill="var(--stripe-dark)"/>
    </svg>

    <div class="back-brand">
      <span class="brand-dot"></span>
      <span class="brand-name">Meridale Cleaning Services</span>
    </div>

    <div class="website">meridalecleaningservices.com.au</div>
  </section>

  <div class="side-label side-label--back">Back</div>
</body>
</html>
```